Movie Poster for Short Film Sci-Fi Drama

BrightHollow Pictures of North Carolina is making a new short film called "A Letter Under Paint".

This is short film about a lonely boy who falls in love with a girl from the past through poetry on a closet wall.

I want the poster to invoke longing and love. I want the focus of the poster to be poetry on a closet wall and I want the words from title of the movie to be part of the poetry written on the walls, but to stand out as the title somehow.

This is not a happy-go-lucky romantic comedy. The girl is from 1981 and boy is from the present era.

Because this is a promotional movie poster for a film that has not yet been shot, I do not want any humans featured in the poster. I would like to keep the focus on the handwritten poetry that sparked a romance between two teenagers decades apart in time.

I would like to have "A BrightHollow Production" at the top of the poster, please.

Target Market(s)

Teenagers upward to adults.

Industry/Entity Type

Movie Production

Requirements
Must have
• Handwriting font.
Should not have
• Humans or faces; exterior walls

```html
<!DOCTYPE html>
<html lang="en">
<head>
<meta charset="utf-8">
<title>A Letter Under Paint — Poster</title>
<link rel="stylesheet" href="https://fonts.googleapis.com/css2?family=Alex+Brush&family=Kaushan+Script&display=swap">
<style>
  :root {
    --wall-light: #f3f3f2;
    --wall-mid: #e2e2e0;
    --wall-shade: #cfcfcd;
    --floor-top: #a9a9a7;
    --floor-bottom: #8c8c8a;
    --title-green: #3e5c4f;
    --ink: #3a3a3a;
    --paper: #fafafa;
    --paper-shade: #d9d9d7;
  }
  * { margin: 0; padding: 0; box-sizing: border-box; }
  html, body { width: 810px; height: 1200px; overflow: hidden; }
  body { background: var(--wall-mid); }

  .poster {
    position: relative;
    width: 810px;
    height: 1200px;
    overflow: hidden;
  }

  .wall {
    position: absolute;
    inset: 0 0 100px 0;
    background:
      radial-gradient(ellipse at 55% 45%, var(--wall-light) 0%, var(--wall-mid) 60%, var(--wall-shade) 100%);
  }

  .floor {
    position: absolute;
    left: 0; right: 0; bottom: 0;
    height: 100px;
    background: linear-gradient(var(--floor-top), var(--floor-bottom));
    border-top: 6px solid var(--wall-shade);
  }

  .credit {
    position: absolute;
    top: 142px;
    left: 0; right: 0;
    padding-left: 14px;
    text-align: center;
    font-family: "Alex Brush", cursive;
    font-size: 24px;
    color: var(--ink);
  }

  .title {
    position: absolute;
    top: 240px;
    left: 0; right: 0;
    text-align: center;
    font-family: "Kaushan Script", cursive;
    color: var(--title-green);
    line-height: 1;
  }
  .title span { display: block; }
  .title .title-small { font-size: 64px; }
  .title .title-large { font-size: 150px; }
  .title .title-a { margin-left: 120px; }
  .title .title-letter { margin-top: -6px; }
  .title .title-under { margin-top: 4px; margin-left: 90px; }
  .title .title-paint { margin-top: -4px; }

  .tagline {
    position: absolute;
    top: 846px;
    left: 0; right: 0;
    text-align: center;
    font-family: "Alex Brush", cursive;
    font-size: 33px;
    line-height: 50px;
    color: var(--ink);
  }

  .paper {
    position: absolute;
    background: linear-gradient(135deg, var(--paper) 40%, var(--paper-shade));
    box-shadow: 0 6px 10px rgba(0,0,0,0.12);
  }
  .paper-left { left: 60px; top: 458px; width: 160px; height: 52px; transform: rotate(-8deg); }
  .paper-right { left: 545px; top: 292px; width: 170px; height: 48px; transform: rotate(18deg); opacity: 0.85; }
  .paper-low { left: 426px; top: 742px; width: 120px; height: 42px; transform: rotate(20deg); }
</style>
</head>
<body>
  <main class="poster">
    <div class="wall" role="img" aria-label="Whitewashed brick wall inside a closet"></div>
    <div class="floor" role="img" aria-label="Grey floor at the foot of the wall"></div>

    <p class="credit">A BrightHollow Production</p>

    <h1 class="title">
      <span class="title-small title-a">A</span>
      <span class="title-large title-letter">Letter</span>
      <span class="title-small title-under">Under</span>
      <span class="title-large title-paint">Paint</span>
    </h1>

    <div class="paper paper-left" role="img" aria-label="Loose sheet of paper drifting in the air"></div>
    <div class="paper paper-right" role="img" aria-label="Loose sheet of paper drifting in the air"></div>
    <div class="paper paper-low" role="img" aria-label="Loose sheet of paper drifting in the air"></div>

    <p class="tagline">
      Memories fade away into the wind behind the moon.<br>
      A girl with golden eyes longs to join them very soon.
    </p>
  </main>
</body>
</html>
```